Birchline Tank & Field

Would like to see some single sided ones but would also like to see some double sided with one sided only being the logo. Owners name is Tom Waldrick. Phone number is 555-214-8830
Services are pumping, inspections, installs, and repairs

Contact Information for Business Card

555-241-8830 Tom Waldrick Cedar Hollow, ST

```html
<!DOCTYPE html>
<html lang="en">
<head>
<meta charset="utf-8">
<title>Birchline Tank &amp; Field – Business Card</title>
<link rel="stylesheet" href="https://fonts.googleapis.com/css2?family=Inter:wght@400;800&display=swap">
<style>
  :root {
    --backdrop: #dcdddf;
    --paper: #ecebe8;
    --ink-dark: #0b0b0b;
    --teal: #2bbfb3;
    --text-grey: #6b6b6b;
    --white: #ffffff;
  }
  * { box-sizing: border-box; margin: 0; padding: 0; }
  html, body {
    width: 1200px;
    height: 1051px;
    overflow: hidden;
    background: var(--backdrop);
    font-family: "Inter", Arial, sans-serif;
  }
  .sheet {
    width: 1200px;
    height: 1051px;
    display: flex;
    flex-direction: column;
    align-items: center;
    justify-content: center;
    gap: 60px;
  }
  .card {
    width: 700px;
    height: 400px;
    border-bottom: 6px solid var(--teal);
    box-shadow: 0 14px 30px rgba(0,0,0,0.18);
    position: relative;
  }
  /* Contact side */
  .card--front {
    background: var(--paper);
    display: flex;
    align-items: center;
    padding-left: 130px;
  }
  .identity {
    text-align: right;
    white-space: nowrap;
    align-self: center;
    margin-top: -60px;
  }
  .identity__name {
    color: var(--teal);
    font-weight: 800;
    font-size: 22px;
    letter-spacing: -0.3px;
    text-transform: uppercase;
    line-height: 1.1;
  }
  .identity__role {
    color: var(--text-grey);
    font-size: 14px;
    margin-top: 4px;
  }
  .divider {
    width: 2px;
    height: 104px;
    background: var(--teal);
    margin: 40px 0 0 28px;
    align-self: center;
  }
  .contact-list {
    list-style: none;
    margin: 44px 0 0 22px;
    display: flex;
    flex-direction: column;
    gap: 5px;
  }
  .contact-list__item {
    display: flex;
    align-items: center;
    gap: 8px;
    color: var(--text-grey);
    font-size: 14px;
    white-space: nowrap;
  }
  .contact-list__icon { width: 12px; height: 12px; fill: var(--teal); flex: none; }
  /* Brand side */
  .card--back {
    background: var(--ink-dark);
    display: flex;
    align-items: center;
    justify-content: center;
  }
  .brand {
    display: flex;
    align-items: center;
    gap: 16px;
    color: var(--white);
    font-weight: 800;
    font-size: 34px;
    letter-spacing: 1px;
    text-transform: uppercase;
    white-space: nowrap;
  }
  .brand__dot {
    width: 18px; height: 18px;
    border-radius: 50%;
    background: var(--teal);
  }
</style>
</head>
<body>
<main class="sheet">
  <section class="card card--front" aria-label="Business card contact side">
    <div class="identity">
      <p class="identity__name">Tom Waldrick</p>
      <p class="identity__role">Founder / CEO</p>
    </div>
    <div class="divider"></div>
    <ul class="contact-list">
      <li class="contact-list__item">
        <svg class="contact-list__icon" viewBox="0 0 24 24"><path d="M6.6 10.8a15.1 15.1 0 0 0 6.6 6.6l2.2-2.2a1 1 0 0 1 1-.25 11.4 11.4 0 0 0 3.6.57 1 1 0 0 1 1 1V20a1 1 0 0 1-1 1A17 17 0 0 1 3 4a1 1 0 0 1 1-1h3.5a1 1 0 0 1 1 1c0 1.25.2 2.45.57 3.57a1 1 0 0 1-.25 1z"/></svg>
        555-241-8830
      </li>
      <li class="contact-list__item">
        <svg class="contact-list__icon" viewBox="0 0 24 24"><path d="M2 5h20v14H2z M2 5l10 8 10-8"/></svg>
        info@birchlinetank.com
      </li>
      <li class="contact-list__item">
        <svg class="contact-list__icon" viewBox="0 0 24 24"><circle cx="12" cy="12" r="10"/></svg>
        www.birchlinetank.com
      </li>
      <li class="contact-list__item">
        <svg class="contact-list__icon" viewBox="0 0 24 24"><path d="M12 2a7 7 0 0 0-7 7c0 5 7 13 7 13s7-8 7-13a7 7 0 0 0-7-7zm0 9.5A2.5 2.5 0 1 1 12 6.5a2.5 2.5 0 0 1 0 5z"/></svg>
        Cedar Hollow, ST
      </li>
    </ul>
  </section>

  <section class="card card--back" aria-label="Business card brand side">
    <div class="brand">
      <span class="brand__dot"></span>
      <span class="brand__name">Birchline Tank &amp; Field</span>
    </div>
  </section>
</main>
</body>
</html>
```